Saffron Lantern Court Business Card

I am looking for a business card desgined for my restaurant. It is an Indian restaurant, we are looking for something thats modern, yet traditional with the indian culture, we are looking for colors that match our logo. The logo is a design of the building with the name of the restaurant. for more information on the restaurant go to www.saffronlanterncourt.example

Industry/Entity Type

Indian Restaurant

Contact Information for Business Card

we are looking for somthing thats modern, yet traditional with the indian culture, we are looking for colors that match our logo. The logo is a design of the building with the name of the restaurant. for more information on the restaurant go to www.saffronlanterncourt.example

Requirements
Must have
• The logo that is attached,
• Name: Harvinder Oberoi,
• address of the restaurant: 7328 West Larkspur Rd, Larkspur Vale, Arizona, 85099
• Phone: (602) 555-0147
• Fax: (602) 555-0193
• Restaurant Catering Banquet
• Website: www.SaffronLanternCourt.example
Nice to have
• wanted to get something that goes with the theme of the restaurant, which is traditional but also keep a very professional and modern touch

```html
<!DOCTYPE html>
<html lang="en">
<head>
<meta charset="utf-8">
<title>Saffron Lantern Court – Business Card</title>
<link rel="stylesheet" href="https://fonts.googleapis.com/css2?family=Open+Sans:wght@400;600;700&display=swap">
<style>
  :root {
    --backdrop: #8a8a8a;
    --card: #f4f4f2;
    --maroon: #8a1f1f;
    --rust: #b4452a;
    --ink: #3a3a3a;
    --shadow: rgba(0, 0, 0, 0.28);
  }
  * { box-sizing: border-box; margin: 0; padding: 0; }
  html, body {
    width: 1200px;
    height: 818px;
    overflow: hidden;
    background: var(--backdrop);
    font-family: "Open Sans", Arial, sans-serif;
  }
  .sheet {
    width: 1200px;
    height: 818px;
    display: flex;
    align-items: center;
    justify-content: center;
    gap: 60px;
    padding: 0 50px;
  }
  .card {
    width: 520px;
    height: 298px;
    background: var(--card);
    box-shadow: 0 10px 24px var(--shadow);
    position: relative;
  }
  .card--front {
    display: flex;
    align-items: center;
    justify-content: center;
  }
  .brand-name {
    color: var(--maroon);
    font-weight: 700;
    font-size: 38px;
    line-height: 1.12;
    letter-spacing: 3px;
    text-transform: uppercase;
    text-align: center;
  }
  .holder {
    position: absolute;
    top: 30px;
    right: 30px;
    text-align: right;
  }
  .holder__name {
    color: var(--maroon);
    font-weight: 700;
    font-size: 17px;
    letter-spacing: 0.5px;
    text-transform: uppercase;
  }
  .holder__role {
    color: var(--rust);
    font-weight: 400;
    font-size: 13px;
  }
  .contact {
    position: absolute;
    left: 32px;
    top: 92px;
    color: var(--ink);
    font-size: 13px;
    line-height: 1.5;
    font-style: normal;
  }
  .contact__label { font-weight: 700; }
  .contact__web {
    font-weight: 700;
    text-transform: uppercase;
  }
</style>
</head>
<body>
  <main class="sheet">
    <section class="card card--front" aria-label="Card front">
      <h1 class="brand-name">Saffron<br>Lantern<br>Court</h1>
    </section>

    <section class="card card--back" aria-label="Card back">
      <div class="holder">
        <p class="holder__name">Harvinder Oberoi</p>
        <p class="holder__role">Restaurant Catering Banquet</p>
      </div>
      <address class="contact">
        <p>7328 West Larkspur Rd</p>
        <p>Larkspur Vale, Arizona, 85099</p>
        <p><span class="contact__label">PHONE</span> (602) 555-0147</p>
        <p><span class="contact__label">FAX</span> (602) 555-0193</p>
        <p class="contact__web">saffronlanterncourt.example</p>
      </address>
    </section>
  </main>
</body>
</html>
```